Copper Moth Tattoo

Business card / Appointment card in one

Ive attached the new logo along with a simple format of what I would like written out on the back! Would like a clean/ modern style font to be used! I also attached the current card for a reference of style!

The colors of this would be either white and gold lettering or black with gold lettering.

Email - CopperMothKV@inkmail-demo.com
Ph # 555-482-7319

The message at bottom of back - All cancellations or No Call No Shows within 48 hours of appointment time will result in a forfeit of deposit.

Small block avail (if card is black) to write in appointment date/time

Target Market(s)

Card for Tattoo shop

Contact Information for Business Card

in project description area!

Font styles to use
Sans Serif

Requirements
Must have
• Please refer to current business card photos that were attached as well!
Nice to have
• Looking for blacks, greys and gold for color scheme

```html
<!DOCTYPE html>
<html lang="en">
<head>
<meta charset="utf-8">
<title>Copper Moth Tattoo – Business &amp; Appointment Card</title>
<link rel="stylesheet" href="https://fonts.googleapis.com/css2?family=UnifrakturMaguntia&family=Pinyon+Script&family=Lato:wght@400;700&display=swap">
<style>
  :root {
    --stage: #2a2b30;
    --card-black: #0b0b0c;
    --card-black-soft: #1e1e20;
    --marble-dark: #141212;
    --marble-mid: #2b2624;
    --gold: #e9b72f;
    --gold-light: #f6d872;
    --white: #ffffff;
    --ink: #111111;
    --rule: #3a3a3a;
  }
  html, body {
    margin: 0;
    padding: 0;
    width: 1200px;
    height: 864px;
    overflow: hidden;
    background: var(--stage);
  }
  .canvas {
    position: relative;
    width: 1200px;
    height: 864px;
  }
  .card {
    position: absolute;
    border-radius: 20px;
    overflow: hidden;
    box-shadow: 0 18px 40px rgba(0,0,0,0.45);
  }
  /* Front */
  .card-front {
    left: 70px;
    top: 272px;
    width: 560px;
    height: 320px;
  }
  .marble-fill {
    position: absolute;
    inset: 0;
    background: radial-gradient(ellipse at 40% 40%, var(--marble-mid) 0%, var(--marble-dark) 70%);
  }
  .front-name {
    position: absolute;
    inset: 0;
    display: flex;
    align-items: center;
    justify-content: center;
    font-family: "UnifrakturMaguntia", serif;
    font-size: 46px;
    color: var(--gold);
  }
  /* Back */
  .card-back {
    left: 780px;
    top: 152px;
    width: 330px;
    height: 560px;
    background: var(--white);
  }
  .back-contact {
    position: absolute;
    left: 0;
    top: 0;
    width: 100%;
    height: 330px;
    background: linear-gradient(180deg, var(--card-black) 0%, var(--card-black-soft) 100%);
    box-sizing: border-box;
    padding: 46px 24px 0 24px;
    text-align: center;
  }
  .shop-name {
    margin: 0;
    font-family: "UnifrakturMaguntia", serif;
    font-weight: 400;
    font-size: 52px;
    line-height: 1;
    color: var(--gold);
  }
  .shop-kind {
    margin: 6px 0 0;
    font-family: "UnifrakturMaguntia", serif;
    font-size: 34px;
    line-height: 1;
    color: var(--gold);
  }
  .contact-line {
    margin: 0;
    font-family: "Pinyon Script", cursive;
    color: var(--white);
  }
  .contact-email {
    margin-top: 30px;
    font-size: 19px;
  }
  .contact-phone {
    margin-top: 6px;
    font-size: 28px;
  }
  .appointment {
    position: absolute;
    left: 0;
    top: 330px;
    width: 100%;
    height: 230px;
    box-sizing: border-box;
    padding: 20px 26px 0 26px;
    color: var(--ink);
  }
  .appointment-title {
    margin: 0;
    text-align: right;
    font-family: "UnifrakturMaguntia", serif;
    font-size: 20px;
  }
  .field {
    display: flex;
    align-items: flex-end;
    gap: 10px;
    margin-top: 10px;
    font-family: "Lato", sans-serif;
    font-size: 14px;
  }
  .field-line {
    flex: 1;
    border-bottom: 1.5px solid var(--rule);
    height: 14px;
  }
  .policy {
    margin: 20px 0 0;
    font-family: "Lato", sans-serif;
    font-size: 14px;
    line-height: 1.4;
  }
</style>
</head>
<body>
  <main class="canvas">
    <section class="card card-front">
      <div class="marble-fill" role="img" aria-label="Black marble texture with fine white veins"></div>
      <div class="front-name">Copper Moth Tattoo</div>
    </section>

    <section class="card card-back">
      <div class="back-contact">
        <h1 class="shop-name">Copper Moth</h1>
        <p class="shop-kind">Tattoo</p>
        <p class="contact-line contact-email">CopperMothKV@inkmail-demo.com</p>
        <p class="contact-line contact-phone">№ 555-482-7319</p>
      </div>
      <div class="appointment">
        <p class="appointment-title">Appointment</p>
        <div class="field"><span>Time</span><span class="field-line"></span></div>
        <div class="field"><span>Date</span><span class="field-line"></span></div>
        <p class="policy">All cancellations or No Call No Shows within 48 hours of appointment time will result in a forfeit of deposit.</p>
      </div>
    </section>
  </main>
</body>
</html>
```